Moroccan Wordpress Keluma Exhibit Design

We seek a new website for Keluma (VarenStoneQuest.org), an exhibit of The Tolvek Initiative’s Atlas Hall of Coastal Heritage Ways, dedicated to uncovering the “buried” or “covered” Jewish treasures of Morocco.
Spanning the entire country, from metropolitan centers to remote villages, Keluma proffers a virtual passport to visitors wishing to explore mountain-top shrines of Jewish “saints” that continue to be voluntarily protected by Muslim caretakers, scorpion-guarded genizot (burial grounds for holy texts and objects), anthropomorphic tombstones in seaside cemeteries, synagogues on the edge of the Sahara Desert, and ancient urban quarters with hidden reminders of their one-time residents.
This exhibit marks the first public showing of documentation on the majority of these sites, including several Vichy regime desert labor and “discipline” camps where hundreds of Jews and non-Jewish political prisoners toiled, suffered torture, and died during the Holocaust.
Keluma is certainly the first to feature:
* Extensive documentation on Jewish sites in major cities and remote settings alike;
* Exclusive immersive panoramas, three-dimensional reconstructions, high-definition videos, site summaries, cultural atlas, archival and contemporary photos; and
* Interactive virtual tours of sites led by Morocco’s only Jewish guide.
Keluma's website design needs to be clean and informational and exciting as well as showcase the best of our collection. The winning design should include an intuitive interface and taxonomy capable of handling hundreds of site entries.
The template should also have a distinctive homepage, themed pages (curator's introduction, staff, screening rooms to view multimedia content, virtual tours, behind-the-scenes, contribute), and no blog elements (e.g., comment section). Admin friendliness is a plus.

```html
<!DOCTYPE html>
<html lang="en">
<head>
<meta charset="utf-8">
<title>Keluma — Jewish Treasures of Southern Morocco</title>
<link rel="stylesheet" href="https://fonts.googleapis.com/css2?family=Lora:ital,wght@0,400;0,700;1,400;1,700&family=Arimo:wght@400;700&family=Open+Sans:wght@400;600&display=swap">
<style>
:root{
  --parchment-deep:#b08a3e;
  --parchment-mid:#d2b46f;
  --page:#ece3cf;
  --page-light:#f1eadb;
  --footer-bg:#e4dac4;
  --ink:#5b4a35;
  --heading:#6b3d0c;
  --brand-red:#8b1c1c;
  --nav-bg:#120d08;
  --nav-text:#f0b100;
  --link:#c4893a;
  --bar:#2b2218;
  --rule:#cdbf9f;
}
*{margin:0;padding:0;box-sizing:border-box}
html,body{width:800px;height:1200px;overflow:hidden}
body{
  position:relative;
  background:radial-gradient(ellipse at 50% 40%,var(--parchment-mid),var(--parchment-deep) 85%);
  font-family:"Arimo",Arial,sans-serif;color:var(--ink);
}
.page{position:absolute;left:117px;top:0;width:570px;height:1183px;background:var(--page)}
.masthead{height:75px;background:var(--page-light);position:relative}
.brand{position:absolute;left:18px;top:10px;font-family:"Lora",Georgia,serif;font-weight:700;font-size:40px;line-height:48px;color:var(--brand-red);letter-spacing:1px;white-space:nowrap}
.tagline-title{position:absolute;left:194px;top:30px;font-family:"Lora",Georgia,serif;font-style:italic;font-weight:700;font-size:17px;line-height:20px;color:var(--brand-red);white-space:nowrap}
.presented{position:absolute;left:203px;top:52px;font-family:"Arimo",Arial,sans-serif;font-weight:700;font-size:10px;line-height:12px;color:var(--brand-red);white-space:nowrap}
.nav{height:22px;background:var(--nav-bg);display:flex;align-items:center;padding-left:31px;gap:15px;white-space:nowrap;overflow:hidden}
.nav a{color:var(--nav-text);text-decoration:none;font-weight:700;font-size:10.5px;line-height:22px;white-space:nowrap;flex:none}
.slider{position:relative;height:214px}
.slide-photo{position:absolute;inset:0;background:linear-gradient(90deg,#3a1d10 0%,#6a3b1a 18%,#c8962e 42%,#e2bf52 52%,#b07a26 64%,#5a2c14 80%,#c86a20 90%,#3a1a0e 100%)}
.slide-arrow{position:absolute;top:50px;width:18px;height:18px}
.caption{position:absolute;left:0;right:0;bottom:0;height:22px;background:rgba(20,12,6,.75);text-align:center;font-family:"Lora",Georgia,serif;font-style:italic;font-size:11.5px;color:var(--nav-text);line-height:22px}
.intro{position:absolute;top:343px;left:0;right:0;text-align:center;font-family:"Lora",Georgia,serif;font-style:italic;font-weight:700;font-size:14.5px;color:var(--heading);white-space:nowrap}
.posts{position:absolute;left:18px;top:393px;width:340px}
.post{position:relative;height:114px}
.post::after{content:"";position:absolute;left:90px;top:113px;width:156px;height:1px;background:var(--rule)}
.post:last-child::after{display:none}
.post .thumb{position:absolute;left:0;top:0;width:90px;height:91px;border:2px solid #8a4a1c}
.post .body{position:absolute;left:111px;top:0;width:228px}
.post h2{font-family:"Lora",Georgia,serif;font-style:italic;font-weight:700;font-size:15px;line-height:18px;color:var(--heading);margin-bottom:3px}
.post p{font-size:7.4px;line-height:10px;color:#6d5d48}
.post .more{display:block;margin-top:4px;font-size:7.5px;font-weight:700;color:#2a1e12;text-decoration:none}
.pager{position:absolute;left:18px;top:962px;font-size:6.5px;color:#7a6a54;display:flex;align-items:center;gap:5px}
.pager span.num{display:inline-block;border:1px solid var(--rule);padding:1px 4px;background:var(--page-light)}
.sidebar{position:absolute;left:404px;top:392px;width:150px}
.sidebar h3{font-family:"Lora",Georgia,serif;font-style:italic;font-weight:700;font-size:11.5px;color:var(--heading);margin-bottom:14px}
.search{height:17px;border:1px solid var(--rule);background:var(--page-light);font-size:7px;padding:3px 4px;position:relative;margin-bottom:16px}
.search svg{position:absolute;right:4px;top:3px}
.recent{display:flex;gap:11px;margin-bottom:22px}
.recent div{width:36px;height:36px;border:1px solid #fff}
.sidebar ul{list-style:none}
.sidebar li{font-size:7.5px;color:var(--link);margin-bottom:7px;font-family:"Open Sans",Arial,sans-serif;white-space:nowrap}
.footer{position:absolute;left:0;top:993px;width:570px;height:167px;background:var(--footer-bg);border-top:1px solid var(--rule)}
.footer .col{position:absolute;top:21px;width:125px}
.footer h4{font-family:"Open Sans",Arial,sans-serif;font-weight:600;font-size:8.5px;color:#5a4a36;margin-bottom:12px}
.footer li{list-style:none;font-family:"Open Sans",Arial,sans-serif;font-size:7.2px;color:#6a5a46;margin-bottom:10px;white-space:nowrap}
.footer p{font-family:"Open Sans",Arial,sans-serif;font-size:7px;line-height:11px;color:#8a7a64}
.legal{position:absolute;left:0;top:1160px;width:570px;height:23px;background:var(--bar);color:#e6dcc8;font-size:6.5px;font-weight:700;text-align:center;line-height:23px}
</style>
</head>
<body>
<div class="page">
  <header class="masthead">
    <div class="brand">Keluma</div>
    <div class="tagline-title">Jewish Treasures of Southern Morocco</div>
    <div class="presented">Presented by the Tolvek Initiative and the Marlowe Foundation</div>
  </header>
  <nav class="nav">
    <a href="#">Welcome to Keluma</a><a href="#">Comming Soon</a><a href="#">About</a><a href="#">Guided Tours</a><a href="#">Panoramas</a><a href="#">Interviews</a><a href="#">Contact</a>
  </nav>
  <section class="slider">
    <div class="slide-photo" role="img" aria-label="Photo of a synagogue interior with a carved golden ark and stained glass windows"></div>
    <svg class="slide-arrow" style="left:7px" viewBox="0 0 18 18"><circle cx="9" cy="9" r="9" fill="rgba(255,255,255,.35)"/><path d="M11 5 L7 9 L11 13" stroke="#333" stroke-width="2" fill="none"/></svg>
    <svg class="slide-arrow" style="right:7px" viewBox="0 0 18 18"><circle cx="9" cy="9" r="9" fill="rgba(255,255,255,.35)"/><path d="M7 5 L11 9 L7 13" stroke="#333" stroke-width="2" fill="none"/></svg>
    <div class="caption">Interior, Rabat Synagogue</div>
  </section>

  <div class="intro">Years of work and contributions by an array of people...</div>

  <main class="posts">
    <article class="post">
      <div class="thumb" role="img" aria-label="Photo of a whitewashed desert synagogue" style="background:linear-gradient(#d9c3a4,#b98e62)"></div>
      <div class="body"><h2>Sinagogues</h2><p>According to legend, a band of Jews fleeing the destruction of the Temple in Jerusalem headed west, eventually arriving at this oasis at the foot of a sloping mountain along the edge of the Sahara desert. Having experienced the magnificent temple in Jerusalem, they are said to have created an independent Jewish realm and built a mini-temple of their own...</p><a class="more" href="#">Read More &gt;&gt;</a></div>
    </article>
    <article class="post">
      <div class="thumb" role="img" aria-label="Photo of a hillside cemetery under a blue sky" style="background:linear-gradient(#9fb7cf 30%,#b6764a 60%,#8a5434)"></div>
      <div class="body"><h2>Cemeteries</h2><p>At first glance, all visitors see is a field of stones that is reminiscent of the surface of Mars. But this lonely cemetery, perched above a wadi and below a mountain at the edge of the Sahara desert, contains hundreds of graves. Out of the initial disorder, the shape of tombs begins to emerge and bits of Hebrew writing poke out of the rubble...</p><a class="more" href="#">Read More &gt;&gt;</a></div>
    </article>
    <article class="post">
      <div class="thumb" role="img" aria-label="Photo of a shrine interior with a caretaker" style="background:linear-gradient(135deg,#c9c2b4,#5c6a78 60%,#8a7c68)"></div>
      <div class="body"><h2>Shrines</h2><p>Perched on the edge of a mountain above a river valley sits the 500 year-old tomb of an emissary from the land of Israel who died while on a fundraising trip in southern Morocco. The Rabbi Adiel (Aaron) later given the moniker "Ben Orsal" ("Son of the Stream") and remains one of the most revered Jewish saints in Morocco, including by Muslims, who call him "Mul Tazrit"...</p><a class="more" href="#">Read More &gt;&gt;</a></div>
    </article>
    <article class="post">
      <div class="thumb" role="img" aria-label="Photo of a ruined water tower at a former labor camp" style="background:linear-gradient(#b9c3cc 35%,#b08d62 65%,#8f6e4c)"></div>
      <div class="body"><h2>Vichy Camps</h2><p>The small town of Tendrara is the site of a Vichy era labor camp, built along the railroad stretching from Oran, Algeria, south through Morocco's eastern border. The railroad was largely built by the labor of Vichy prisoners, sent to camps like this one. It is the best-preserved Vichy camp along Morocco's eastern border with Algeria, perhaps in the country...</p><a class="more" href="#">Read More &gt;&gt;</a></div>
    </article>
    <article class="post">
      <div class="thumb" role="img" aria-label="Photo of crumbling mud-brick buildings in an oasis" style="background:linear-gradient(135deg,#9a6e52,#5a3a2a 55%,#b48c6c)"></div>
      <div class="body"><h2>Other Sites</h2><p>Figuig is an island of Morocco surrounded by Algeria. Located in southeastern Morocco, Figuig is a town composed of seven different communities, amid a leafy palm oasis in the shadow of Algerian peaks and desert. Like many oasis in southern Morocco, Figuig once had a small Jewish population, reportedly numbering about one hundred Jews in its mellah (Jewish quarter)...</p><a class="more" href="#">Read More &gt;&gt;</a></div>
    </article>
  </main>

  <div class="pager">Page 1 of 2 <span class="num">1</span><span class="num">2</span></div>

  <aside class="sidebar">
    <h3>Language</h3>
    <div class="search">Search<svg width="9" height="9" viewBox="0 0 10 10"><circle cx="4" cy="4" r="3" stroke="#aaa" fill="none" stroke-width="1.3"/><path d="M6.3 6.3 L9 9" stroke="#aaa" stroke-width="1.3"/></svg></div>
    <h3>Recent pictures</h3>
    <div class="recent">
      <div role="img" aria-label="Thumbnail photo of a doorway" style="background:linear-gradient(#9fb0bf,#c8b89a)"></div>
      <div role="img" aria-label="Thumbnail photo of a courtyard" style="background:linear-gradient(#6d7a5a,#b8a682)"></div>
      <div role="img" aria-label="Thumbnail photo of a white building" style="background:linear-gradient(#8aa6c2,#e2ddd2)"></div>
    </div>
    <h3>What is new?</h3>
    <ul><li>Molestie lobortis egestas</li><li>In volutpat lacinia consequat</li><li>Integer molestie sem non</li><li>In volutpat lacinia</li><li>Ut varius diam sit</li></ul>
  </aside>

  <footer class="footer">
    <div class="col" style="left:19px"><h4>Recent Posts</h4><ul><li>Molestie lobortis egestas</li><li>In volutpat lacinia consequat</li><li>Integer molestie sem non</li><li>In volutpat lacinia</li><li>Ut varius diam sit</li></ul></div>
    <div class="col" style="left:155px"><h4>Recent Posts</h4><ul><li>Molestie lobortis egestas</li><li>In volutpat lacinia consequat</li><li>Integer molestie sem non</li><li>In volutpat lacinia</li><li>Ut varius diam sit</li></ul></div>
    <div class="col" style="left:291px"><h4>Recent Posts</h4><ul><li>Molestie lobortis egestas</li><li>In volutpat lacinia consequat</li><li>Integer molestie sem non</li><li>In volutpat lacinia</li><li>Ut varius diam sit</li></ul></div>
    <div class="col" style="left:427px;width:125px"><h4>About</h4><p>Lorem ipsum dolor sit amet, consectetur adipiscing elit. Nam et arcu velit. Vestibulum semper dui eget lorem pellentesque sit amet volutpat tortor sollicitudin. Praesent vehicula neque vitae nisi auctor sed pharetra dolor rutrum.</p></div>
  </footer>
  <div class="legal">Copyright © 2010 Coastline Record Works, Inc. All Rights Reserved.</div>
</div>
</body>
</html>
```